Juniper Vale

I need a label design for a Woman's Professional Haircare line sold to salons. So the label would be on Shampoo's, Conditioners , serum's, styling products, bleaches, etc...
I'm looking at a softer color label design like lavender or shades of lighter purple. i would like Logo to be or contain a rose rose. Here are a few designs from the professional ranks that are different. They use the solid colors with the back design. I was thinking something like this might work.

Colors
A7469A
B969AE
D3A5CF
EDDBEB
F8F0F9
6B429C
8869AF
B7A5CE
E3DAEB
F3F0F8

```html
<!DOCTYPE html>
<html lang="en">
<head>
<meta charset="utf-8">
<title>Juniper Vale – Rose Oil Shampoo Labels</title>
<link rel="stylesheet" href="https://fonts.googleapis.com/css2?family=Oswald:wght@500&family=Lato:wght@400;700&family=Crimson+Text:ital@1&family=Open+Sans:wght@600&display=swap">
<style>
  :root {
    --canvas: #d6d6d8;
    --panel: #6b5cb4;
    --panel-deep: #5e4fa8;
    --pattern-light: #d3a5cf;
    --pattern-mid: #b7a5ce;
    --pattern-ink: #8869af;
    --ink-light: #ffffff;
  }
  * { margin: 0; padding: 0; box-sizing: border-box; }
  html, body { width: 1200px; height: 857px; overflow: hidden; }
  body {
    background: var(--canvas);
    display: flex;
    align-items: center;
    justify-content: center;
    gap: 60px;
  }
  .label { position: relative; color: var(--ink-light); text-align: center; }
  .label--tall { width: 240px; height: 620px; }
  .label--jar { width: 420px; height: 300px; }
  .label__art { position: absolute; inset: 0; width: 100%; height: 100%; }
  .label__text { position: absolute; left: 0; right: 0; }
  .brand-mark {
    display: block;
    width: 28px; height: 28px;
    margin: 0 auto 10px;
    border: 1.5px solid var(--ink-light);
    border-radius: 50%;
  }
  .brand-name {
    font-family: "Lato", sans-serif;
    font-weight: 400;
    font-size: 17px;
    letter-spacing: 0.5px;
  }
  .product-name {
    font-family: "Oswald", sans-serif;
    font-weight: 500;
    font-size: 44px;
    line-height: 1.1;
    letter-spacing: 0.5px;
    margin-top: 10px;
    text-transform: uppercase;
  }
  .tagline {
    font-family: "Crimson Text", serif;
    font-style: italic;
    font-size: 15px;
    line-height: 1.35;
    margin-top: 10px;
  }
  .care-note {
    font-family: "Open Sans", sans-serif;
    font-weight: 600;
    font-size: 13px;
    line-height: 1.4;
  }
  .volume {
    font-family: "Oswald", sans-serif;
    font-weight: 500;
    font-size: 15px;
    margin-top: 8px;
  }
  .label--tall .label__head { top: 130px; }
  .label--tall .label__foot { top: 540px; }
  .label--jar .label__head { top: 18px; }
  .label--jar .brand-mark { width: 24px; height: 24px; margin-bottom: 6px; }
  .label--jar .brand-name { font-size: 14px; }
  .label--jar .product-name { font-size: 38px; margin-top: 4px; }
  .label--jar .tagline { font-size: 12px; margin-top: 10px; }
  .label--jar .label__foot { top: 228px; }
  .label--jar .care-note { font-size: 12px; }
  .label--jar .volume { font-size: 13px; margin-top: 4px; }
</style>
</head>
<body>

  <!-- Tube label, geometric pattern variant -->
  <section class="label label--tall">
    <svg class="label__art" viewBox="0 0 240 620" aria-hidden="true">
      <defs>
        <linearGradient id="geoTone" x1="0" y1="0" x2="0" y2="1">
          <stop offset="0" stop-color="#cfa4d4"/>
          <stop offset="1" stop-color="#c19dd0"/>
        </linearGradient>
      </defs>
      <rect class="pattern-fill" width="240" height="520" fill="url(#geoTone)" role="img" aria-label="Geometric lavender mandala pattern"/>
      <path d="M0,150 H50 C80,150 85,100 120,100 C155,100 160,150 190,150 H240 V410 H190 C160,410 155,460 120,460 C85,460 80,410 50,410 H0 Z" fill="var(--panel)"/>
      <path d="M0,162 H52 C82,162 88,113 120,113 C152,113 158,162 188,162 H240" fill="none" stroke="#fff" stroke-width="2"/>
      <path d="M0,398 H52 C82,398 88,447 120,447 C152,447 158,398 188,398 H240" fill="none" stroke="#fff" stroke-width="2"/>
      <rect y="520" width="240" height="100" fill="var(--panel)"/>
      <line x1="0" y1="524" x2="240" y2="524" stroke="#fff" stroke-width="3"/>
    </svg>
    <div class="label__text label__head">
      <span class="brand-mark"></span>
      <p class="brand-name">JUNIPER VALE</p>
      <h2 class="product-name">Rose Oil<br>Shampoo</h2>
      <p class="tagline">Moisturizes Rejuvenates<br>and Restore Strength</p>
    </div>
    <div class="label__text label__foot">
      <p class="care-note">For Dry Damaged<br>Hair Exceptional Care</p>
      <p class="volume">8.5 OZ / 250ML</p>
    </div>
  </section>

  <!-- Bottle label, floral pattern variant -->
  <section class="label label--tall">
    <svg class="label__art" viewBox="0 0 240 620" aria-hidden="true">
      <defs>
        <linearGradient id="floralTone" x1="0" y1="0" x2="1" y2="1">
          <stop offset="0" stop-color="#a98ad0"/>
          <stop offset="1" stop-color="#9a7fc8"/>
        </linearGradient>
      </defs>
      <rect class="pattern-fill" width="240" height="520" fill="url(#floralTone)" role="img" aria-label="Floral paisley pattern in lavender and violet"/>
      <path d="M0,150 H50 C80,150 85,100 120,100 C155,100 160,150 190,150 H240 V410 H190 C160,410 155,460 120,460 C85,460 80,410 50,410 H0 Z" fill="var(--panel-deep)"/>
      <path d="M0,162 H52 C82,162 88,113 120,113 C152,113 158,162 188,162 H240" fill="none" stroke="#fff" stroke-width="2"/>
      <path d="M0,398 H52 C82,398 88,447 120,447 C152,447 158,398 188,398 H240" fill="none" stroke="#fff" stroke-width="2"/>
      <rect y="520" width="240" height="100" fill="var(--panel-deep)"/>
      <line x1="0" y1="524" x2="240" y2="524" stroke="#fff" stroke-width="3"/>
    </svg>
    <div class="label__text label__head">
      <span class="brand-mark"></span>
      <p class="brand-name">JUNIPER VALE</p>
      <h2 class="product-name">Rose Oil<br>Shampoo</h2>
      <p class="tagline">Moisturizes Rejuvenates<br>and Restore Strength</p>
    </div>
    <div class="label__text label__foot">
      <p class="care-note">For Dry Damaged<br>Hair Exceptional Care</p>
      <p class="volume">8.5 OZ / 250ML</p>
    </div>
  </section>

  <!-- Jar label -->
  <section class="label label--jar">
    <svg class="label__art" viewBox="0 0 420 300" aria-hidden="true">
      <defs>
        <linearGradient id="jarTone" x1="0" y1="0" x2="1" y2="1">
          <stop offset="0" stop-color="#a98ad0"/>
          <stop offset="1" stop-color="#9a7fc8"/>
        </linearGradient>
      </defs>
      <rect class="pattern-fill" width="420" height="300" fill="url(#jarTone)" role="img" aria-label="Floral paisley pattern in lavender and violet"/>
      <path d="M0,0 H420 V168 H320 C280,168 270,212 210,212 C150,212 140,168 100,168 H0 Z" fill="var(--panel)"/>
      <path d="M0,158 H102 C142,158 152,201 210,201 C268,201 278,158 318,158 H420" fill="none" stroke="#fff" stroke-width="2"/>
    </svg>
    <div class="label__text label__head">
      <span class="brand-mark"></span>
      <p class="brand-name">JUNIPER VALE</p>
      <h2 class="product-name">Rose Oil Shampoo</h2>
      <p class="tagline">Moisturizes Rejuvenates<br>and Restore Strength</p>
    </div>
    <div class="label__text label__foot">
      <p class="care-note">For Dry Damaged<br>Hair Exceptional Care</p>
      <p class="volume">8.5 OZ / 250ML</p>
    </div>
  </section>

</body>
</html>
```